Web Design Project

We are looking for a new site design for the VELTO Canada. The current site can be found at
http://www.veltocanada-example.org/
The URL is provided for reference. We want a completely different look and layout which is shown in the specifications document.
As part of the design, we want a home page, and inside page.
The design you provide will be implemented in Joomla. The design winner will only need to provide the PSD. We anticipate creating the template coding in-house.
However, if you have experience creating Joomla templates, please let us know as we may ask you to bid separately to do that phase of the project.
We've provided a specifications document which includes wireframes of the home page, and inside page. We've also included a logo file.
For the header at the top, as indicated in the specs document, we want to keep the same overall treatment to every page. We want a graphic treatment with the logo for the header area. In this manner, the design will be flexiable and can be used for future years.
For the home page, we've indicated that we'd like to have a slider implemented within the design.
The wireframe is provided to illustrate the placement of content and menu items. The exact dimensions of each component can be revised as you see fit. We are also flexiable if you feel we have missed items.

```html
<!DOCTYPE html>
<html lang="en">
<head>
<meta charset="utf-8">
<title>VELTO Canada</title>
<link href="https://fonts.googleapis.com/css2?family=Noto+Sans:wght@400;700&family=Open+Sans:ital,wght@0,600;1,700;1,800&family=Roboto+Slab:wght@700&display=swap" rel="stylesheet">
<style>
:root{
  --red:#e23234;
  --red-dark:#c8191c;
  --navy:#2b3f78;
  --navy-soft:#5669a3;
  --ink:#1c1c1c;
  --grey-text:#444;
  --silver-1:#f4f4f4;
  --silver-2:#b9b9b9;
  --silver-3:#8e8e8e;
  --card:#e4e7ef;
  --white:#fff;
  --date:#8b0d0d;
}
*{box-sizing:border-box;margin:0;padding:0}
html,body{width:1200px;height:696px;overflow:hidden;background:var(--white)}
body{position:relative;font-family:"Noto Sans",Verdana,sans-serif;color:var(--ink)}
a{color:inherit;text-decoration:none}

.site-header{position:absolute;left:0;top:0;width:1200px;height:106px;
  background:linear-gradient(#39508c 0,#a9b4d0 3px,#fff 30px,#fff 62px,#d6dbea 88px,#7f8fbb 96px,#33487f 104px,#33487f 106px)}
.brand{position:absolute;left:140px;top:12px;display:flex;align-items:center;gap:8px}
.brand-mark{width:22px;height:22px;border-radius:50%;background:var(--navy)}
.brand-name{font-family:"Open Sans",sans-serif;font-weight:600;font-size:28px;color:var(--navy);letter-spacing:1px}
.utility-nav{position:absolute;right:144px;top:28px;font-size:11.5px;color:#222}
.utility-nav span{margin:0 7px;color:#777;font-size:9px}

.main-nav{position:absolute;left:0;top:106px;width:1200px;height:30px;background:var(--red);border-top:1px solid #f05a5a}
.main-nav ul{list-style:none;display:flex;gap:19px;position:absolute;left:155px;top:7px}
.main-nav a{font-family:"Open Sans",sans-serif;font-weight:600;font-size:11.8px;color:var(--white)}

.hero{position:absolute;left:136px;top:136px;width:928px;height:152px;
  background:linear-gradient(180deg,#e9c9a0 0,#b8a58c 18%,#6d6b5c 45%,#3c4a3e 62%,#58646a 78%,#2f3536 100%)}
.hero-line{position:absolute;font-family:"Open Sans",sans-serif;font-weight:700;font-size:28px;letter-spacing:-1px;
  color:#4f8fe6;-webkit-text-stroke:1px #fff;text-shadow:0 2px 3px rgba(0,0,0,.5)}
.hero-line.one{left:18px;top:74px}
.hero-line.two{left:75px;top:103px}

.side-box{position:absolute;left:138px;width:176px;background:linear-gradient(#e8393b,#d92a2d);border:1px solid #c61c1f;border-radius:2px}
.tab{position:absolute;left:8px;right:8px;top:-6px;height:26px;border-radius:0 0 60px 60px/0 0 22px 22px;
  background:linear-gradient(#fdfdfd,#d1d1d1 60%,#9c9c9c);text-align:center;
  font-family:"Open Sans",sans-serif;font-style:italic;font-weight:700;font-size:12.5px;color:#3a3a3a;line-height:24px}
.sponsors{top:294px;height:134px}
.sponsor-badges{position:absolute;left:18px;top:28px;display:flex;gap:7px}
.badge{width:67px;height:68px;background:var(--white);border:1px solid #ccc;display:flex;align-items:center;justify-content:center}
.badge .shape-square{width:44px;height:40px;background:var(--red-dark)}
.badge .shape-circle{width:56px;height:56px;border-radius:50%;background:radial-gradient(#b7722a,#7a4a1d 70%,#d7a544)}
.arrow{position:absolute;top:56px}
.arrow.prev{left:2px}.arrow.next{right:2px}
.silver-btn{position:absolute;left:17px;width:141px;height:25px;border-radius:3px;
  background:linear-gradient(#eef0f3,#b9c0ca 55%,#9aa3af);box-shadow:0 2px 2px rgba(0,0,0,.3);
  font-family:"Open Sans",sans-serif;font-style:italic;font-weight:700;font-size:14px;color:#6a1033;text-align:center;line-height:25px}
.sponsors .silver-btn{top:102px}

.login{top:437px;height:114px}
.field{position:absolute;left:19px;width:138px;height:20px;border:1px solid #f07d7e;border-radius:3px;
  background:#dc2a2d;color:#f7d0d0;font-size:11px;padding-left:9px;line-height:18px}
.field.user{top:31px}.field.pass{top:55px}
.login .silver-btn{top:80px}

.connected{top:561px;height:73px}
.social{position:absolute;top:34px;width:26px;height:26px;border-radius:4px}
.social.one{left:24px;background:#4a67ad}
.social.two{left:72px;background:#59b5e2}
.social.three{left:126px;background:#1f6fa8}

.welcome{position:absolute;left:331px;top:303px;width:485px}
.welcome h1{font-family:"Open Sans",sans-serif;font-style:italic;font-weight:800;font-size:18px;color:#3d3d3d;letter-spacing:.2px}
.welcome p{margin-top:6px;font-size:11.4px;line-height:16.8px;color:var(--ink)}

.news{position:absolute;left:836px;top:301px;width:227px;height:150px;border:1px solid #d4d4d4;border-radius:3px;
  background:linear-gradient(135deg,#f8f8f8,#dedede)}
.news-tab{position:absolute;left:8px;right:8px;top:-6px;height:55px;border-radius:0 0 80px 80px/0 0 20px 20px;
  background:linear-gradient(#6a6a6a,#9b9b9b 35%,#dedede 80%,#c6c6c6);
  font-family:"Open Sans",sans-serif;font-style:italic;font-weight:800;font-size:18px;color:var(--white);text-align:center;line-height:38px;
  text-shadow:0 1px 2px rgba(0,0,0,.5)}
.news h2{position:absolute;left:13px;top:52px;font-size:12px;font-weight:700;color:#111}
.news p{position:absolute;left:12px;top:70px;width:208px;font-size:10px;line-height:12.5px;color:#111}
.news .date{position:absolute;left:13px;top:114px;font-size:9px;font-weight:700;color:var(--date)}
.news .more{position:absolute;right:18px;top:114px;font-size:9px;color:var(--date)}

.regions{position:absolute;left:332px;top:461px;width:732px;height:172px;border-radius:12px;background:linear-gradient(#e4322f,#d8241f)}
.regions-title{position:absolute;left:14px;top:1px;width:704px;height:27px;background:linear-gradient(#fff,#f0f0f0);
  font-family:"Roboto Slab",serif;font-weight:700;font-size:19px;color:var(--navy);padding-left:17px;line-height:26px}
.region-cards{position:absolute;left:17px;top:39px;display:flex;gap:17px}
.region{width:162px;height:120px;border-radius:3px;border:1px solid #f3b0b0;
  background:linear-gradient(120deg,#d7dbe6,#eef0f6 55%,#cfd4e1)}
.region h3{font-family:"Open Sans",sans-serif;font-style:italic;font-weight:800;font-size:17px;color:var(--red);margin:2px 0 0 6px;letter-spacing:-.4px}
.region ul{list-style:none;margin:2px 0 0 10px}
.region li{font-size:11.4px;line-height:20.8px;color:#111;display:flex;align-items:center;gap:3px}
.bullet{width:12px;height:12px;flex:none}

.footer-nav{position:absolute;left:150px;top:640px;display:flex;align-items:center;gap:8px;font-size:11.6px;color:#222}
.footer-nav .sep{width:9px;height:9px}
.legal{position:absolute;left:390px;top:671px;font-size:11.6px;color:#222}
.legal span{color:var(--navy-soft);margin:0 8px}
</style>
</head>
<body>
<svg width="0" height="0" style="position:absolute">
  <defs>
    <symbol id="bullet" viewBox="0 0 12 12"><circle cx="6" cy="6" r="5.5" fill="#bfc3cb" stroke="#8a8f99"/><path d="M5 3.5 L8 6 L5 8.5Z" fill="#444"/></symbol>
    <symbol id="sep" viewBox="0 0 10 10"><circle cx="5" cy="5" r="3.2" fill="none" stroke="#d42a2a" stroke-width="2.2"/><circle cx="5" cy="5" r="4.6" fill="none" stroke="#d42a2a" stroke-width="1" stroke-dasharray="1.5 1.5"/></symbol>
  </defs>
</svg>

<header class="site-header">
  <a class="brand" href="http://www.veltocanada-example.org/"><span class="brand-mark"></span><span class="brand-name">VELTO</span></a>
  <nav class="utility-nav"><a href="#">Home</a><span>|</span><a href="#">Contact Us</a><span>|</span><a href="#">VELTO International</a></nav>
</header>

<nav class="main-nav">
  <ul>
    <li><a href="#">ABOUT US</a></li><li><a href="#">BOARD</a></li><li><a href="#">CHAPTERS</a></li>
    <li><a href="#">MEMBER SPACE</a></li><li><a href="#">RESOURCES &amp; KNOWLEDGE</a></li>
    <li><a href="#">SPONSORSHIP</a></li><li><a href="#">EXHIBIT</a></li>
  </ul>
</nav>

<section class="hero" role="img" aria-label="Slider photo: city skyline at dusk above a river crossed by bridges">
  <div class="hero-line one">Lorem ipsum dolor sit amet</div>
  <div class="hero-line two">Lorem ipsum dolor sit amet</div>
</section>

<aside class="side-box sponsors">
  <div class="tab">Sponsors</div>
  <svg class="arrow prev" width="12" height="18" viewBox="0 0 12 18"><path d="M10 2 L3 9 L10 16" fill="none" stroke="#fff" stroke-width="3"/></svg>
  <div class="sponsor-badges">
    <div class="badge" role="img" aria-label="Sponsor badge"><div class="shape-square"></div></div>
    <div class="badge" role="img" aria-label="Sponsor award badge"><div class="shape-circle"></div></div>
  </div>
  <svg class="arrow next" width="12" height="18" viewBox="0 0 12 18"><path d="M2 2 L9 9 L2 16" fill="none" stroke="#fff" stroke-width="3"/></svg>
  <a class="silver-btn" href="#">Become a Sponsor</a>
</aside>

<aside class="side-box login">
  <div class="tab">Member Login</div>
  <div class="field user">Username</div>
  <div class="field pass">Password</div>
  <a class="silver-btn" href="#">Login</a>
</aside>

<aside class="side-box connected">
  <div class="tab">Stay Connected</div>
  <a class="social one" href="#" aria-label="Social network one"></a>
  <a class="social two" href="#" aria-label="Social network two"></a>
  <a class="social three" href="#" aria-label="Social network three"></a>
</aside>

<section class="welcome">
  <h1>WELCOME&nbsp; VELTO CANADA</h1>
  <p>Lorem ipsum dolor sit amet, consectetuer adipiscing elit. Nam cursus. Morbi ut miNullam enim leo, egestas id, condimentum at, laoreet mattis, massa. Sed eleifend nonummy diam. Praesent mauris ante, elementum et, bibendum at, posuere sit ametnibh. Duis tincidunt lectus quis dui viverra vestibulum. Suspendisse vulputate aliquam dui. Nulla elementum dui ut augue. Aliquam vehicula mi at mauris. Maecenas placerat, nisl at consequat rhoncus, sem nunc gravida justo, quis eleifend arcu velit quis lacus. Morbi magna magna, tincidunt a, mattis non, imperdiet vitae, tellus.</p>
</section>

<section class="news">
  <div class="news-tab">NEWS AND EVENTS</div>
  <h2>Lorem ipsum dolor sit amet</h2>
  <p>Lorem ipsum dolor sit amet, consectet adipiscing elit Lorem ipsum dolor sit amet, consectet adipiscing elit</p>
  <span class="date">30-01-2013</span>
  <a class="more" href="#">Read more &#10140;</a>
</section>

<section class="regions">
  <h2 class="regions-title">Regions</h2>
  <div class="region-cards">
    <div class="region"><h3>Mountain Pacific</h3><ul>
      <li><svg class="bullet"><use href="#bullet"/></svg>Vancouver Island</li>
      <li><svg class="bullet"><use href="#bullet"/></svg>Vancouver</li>
      <li><svg class="bullet"><use href="#bullet"/></svg>Calgary</li></ul></div>
    <div class="region"><h3>Western</h3><ul>
      <li><svg class="bullet"><use href="#bullet"/></svg>Edmonton</li>
      <li><svg class="bullet"><use href="#bullet"/></svg>Saskatchewan</li>
      <li><svg class="bullet"><use href="#bullet"/></svg>Winnipeg</li></ul></div>
    <div class="region"><h3>Central</h3><ul>
      <li><svg class="bullet"><use href="#bullet"/></svg>National Capital-Ottawa</li>
      <li><svg class="bullet"><use href="#bullet"/></svg>Southwestern Ontario</li>
      <li><svg class="bullet"><use href="#bullet"/></svg>Montreal</li>
      <li><svg class="bullet"><use href="#bullet"/></svg>Toronto</li></ul></div>
    <div class="region"><h3>Atlantic</h3><ul>
      <li><svg class="bullet"><use href="#bullet"/></svg>Nova Scotia</li>
      <li><svg class="bullet"><use href="#bullet"/></svg>Terra-Nova, St. John’s</li>
      <li><svg class="bullet"><use href="#bullet"/></svg>Prince Edward Island</li>
      <li><svg class="bullet"><use href="#bullet"/></svg>Atlantic, St. John’s</li></ul></div>
  </div>
</section>

<footer>
  <nav class="footer-nav">
    <a href="#">Home</a><svg class="sep"><use href="#sep"/></svg>
    <a href="#">About</a><svg class="sep"><use href="#sep"/></svg>
    <a href="#">Board</a><svg class="sep"><use href="#sep"/></svg>
    <a href="#">Chapters</a><svg class="sep"><use href="#sep"/></svg>
    <a href="#">Member Space</a><svg class="sep"><use href="#sep"/></svg>
    <a href="#">Resources &amp; Knowledge</a><svg class="sep"><use href="#sep"/></svg>
    <a href="#">Sponsorship</a><svg class="sep"><use href="#sep"/></svg>
    <a href="#">Exhibit</a><svg class="sep"><use href="#sep"/></svg>
    <a href="#">Member Login</a><svg class="sep"><use href="#sep"/></svg>
    <a href="#">Contact Us</a>
  </nav>
  <p class="legal"><a href="#">Privacy Policy</a><span>|</span>©2009–2013 VELTO Canada Region, All rights reserved</p>
</footer>
</body>
</html>
```